Flyer-Design für  Kampfsportschule
Flyer-Design für Kampfsportschule
Zielgruppe
Wir bieten Taekwondo/Selbstverteidigung an. Meine Zielgruppe sind Erwachsene ab 17 Jahren.
Aufgabenstellung
Das Angebot '1 Monat kostenloses Training, oder einen Monat kostenloses Training' und 'Taekwondo/Selbstverteidigung in Weinstadt' soll eingebracht und direkt sichtbar sein. Eventuell auch Punkte wie Selbstbewusstsein, Beweglichkeit, Zielstrebigkeit, Kraft und Ausdauer, körperliche Fitness... Farben: Weiß, schwarz und Schrift in gelb. Nichts rotes.
Die Daten:
Tel: 0159-4817250 Email: t.m.budohalle@postwelle-mail.de und www.tmbudohalle.de

```html
<!DOCTYPE html>
<html lang="de">
<head>
<meta charset="utf-8">
<title>Taekwondo Selbstverteidigung – 1 Monat kostenloses Training</title>
<link href="https://fonts.googleapis.com/css2?family=Montserrat:wght@300;400;600;700;800;900&display=swap" rel="stylesheet">
<style>
  :root {
    --ink: #222222;
    --ink-deep: #111111;
    --paper: #ffffff;
    --signal: #f7e200;
    --photo-light: #f1f1f1;
    --photo-mid: #d3d3d3;
  }
  * { margin: 0; padding: 0; box-sizing: border-box; }
  html, body { width: 1200px; height: 420px; overflow: hidden; background: var(--ink); }
  .flyer {
    position: relative; width: 1200px; height: 420px; overflow: hidden;
    background: var(--ink); font-family: "Montserrat", sans-serif; color: var(--paper);
  }
  .flyer__backdrop { position: absolute; inset: 0; }
  .action-photo {
    position: absolute; left: 270px; top: 118px; width: 300px; height: 302px;
    border-radius: 140px 140px 0 0;
    background: radial-gradient(ellipse at 50% 55%, var(--photo-mid) 0%, var(--photo-light) 60%, rgba(255,255,255,0) 80%);
  }
  .headline { position: absolute; left: 153px; top: 30px; color: var(--ink-deep); }
  .headline__title { font-weight: 800; font-size: 56px; letter-spacing: -1.5px; line-height: 1; }
  .headline__sub { margin-top: 2px; margin-left: 12px; font-size: 20px; letter-spacing: 8.4px; line-height: 1; }
  .headline__sub-light { font-weight: 400; }
  .headline__sub-bold { font-weight: 900; }
  .offer { position: absolute; left: 696px; top: 40px; }
  .offer__duration { color: var(--signal); font-weight: 900; font-size: 82px; letter-spacing: 10px; line-height: 1; }
  .offer__label { margin-top: -2px; font-weight: 800; font-size: 40px; letter-spacing: -2.2px; line-height: 1; }
  .benefits { position: absolute; left: 697px; top: 196px; list-style: none; }
  .benefits__item {
    display: flex; align-items: center; gap: 6px; height: 18px; margin-bottom: 18px;
    color: var(--signal); font-weight: 600; font-size: 16px; letter-spacing: 2.6px;
  }
  .benefits__item:nth-child(3) { margin-top: 2px; }
  .benefits__tick { width: 30px; height: 26px; margin-top: -8px; }
  .contact { position: absolute; right: 16px; top: 346px; text-align: right; color: var(--ink-deep); }
  .contact__phone { font-weight: 400; font-size: 27px; letter-spacing: -0.5px; line-height: 1; }
  .contact__line { margin-top: 5px; font-weight: 400; font-size: 11px; letter-spacing: 1.3px; line-height: 1.1; text-transform: uppercase; }
  .brand { position: absolute; left: 70px; top: 262px; width: 102px; height: 102px; }
  .brand__circle {
    width: 102px; height: 102px; border-radius: 50%; background: var(--paper);
    display: flex; align-items: center; justify-content: center; text-align: center;
  }
  .brand__name { color: var(--ink-deep); font-weight: 800; font-size: 13px; line-height: 1.15; letter-spacing: 0.5px; }
  .location-tag { position: absolute; left: 16px; top: 376px; width: 206px; height: 30px; }
  .location-tag svg { position: absolute; inset: 0; }
  .location-tag__name {
    position: absolute; left: 60px; top: 3px; color: var(--signal);
    font-weight: 700; font-size: 21px; letter-spacing: 0.3px; line-height: 24px;
  }
</style>
</head>
<body>
<main class="flyer">
  <svg class="flyer__backdrop" width="1200" height="420" viewBox="0 0 1200 420" aria-hidden="true">
    <polygon fill="var(--paper)" points="60,0 475,0 490,30 520,60 540,110 575,150 600,200 640,250 660,300 690,350 712,390 730,420 278,420 250,390 220,350 205,310 180,260 160,230 150,190 120,150 100,110 85,70 70,30"/>
    <polygon fill="var(--ink)" points="60,0 120,0 140,40 170,90 190,130 200,170 225,210 240,260 262,300 280,350 300,420 278,420 250,390 220,350 205,310 180,260 160,230 150,190 120,150 100,110 85,70 70,30"/>
    <polygon fill="var(--signal)" points="730,420 760,410 820,392 880,378 950,362 1010,350 1060,338 1110,310 1160,290 1200,272 1200,420"/>
  </svg>

  <div class="action-photo" role="img" aria-label="Foto: zwei Taekwondo-Kämpfer in weißen Anzügen, einer tritt ein Holzbrett, das der andere hochhält"></div>

  <header class="headline">
    <h1 class="headline__title">Taekwondo</h1>
    <p class="headline__sub"><span class="headline__sub-light">Selbst</span><span class="headline__sub-bold">verteidigung</span></p>
  </header>

  <section class="offer">
    <p class="offer__duration">1 Monat</p>
    <p class="offer__label">kostenloses Training</p>
  </section>

  <ul class="benefits">
    <li class="benefits__item">bleibe fit
      <svg class="benefits__tick" viewBox="0 0 30 26" aria-hidden="true"><path d="M2 15 L8 12 L12 19 Q18 8 29 1 Q20 10 13 25 L10 25 Z" fill="var(--paper)"/></svg>
    </li>
    <li class="benefits__item">lerne dich zu verteidigen
      <svg class="benefits__tick" viewBox="0 0 30 26" aria-hidden="true"><path d="M2 15 L8 12 L12 19 Q18 8 29 1 Q20 10 13 25 L10 25 Z" fill="var(--paper)"/></svg>
    </li>
    <li class="benefits__item">fördere dein Selbstbewusstsein
      <svg class="benefits__tick" viewBox="0 0 30 26" aria-hidden="true"><path d="M2 15 L8 12 L12 19 Q18 8 29 1 Q20 10 13 25 L10 25 Z" fill="var(--paper)"/></svg>
    </li>
  </ul>

  <address class="contact" style="font-style:normal">
    <p class="contact__phone">0159-4817250</p>
    <p class="contact__line">www.tmbudohalle.de</p>
    <p class="contact__line">t.m.budohalle@postwelle-mail.de</p>
  </address>

  <div class="brand">
    <div class="brand__circle"><span class="brand__name">T.M.<br>Budohalle</span></div>
  </div>

  <div class="location-tag">
    <svg width="206" height="30" viewBox="0 0 206 30" aria-hidden="true">
      <polygon points="10,0 206,0 190,30 0,30" fill="var(--ink-deep)"/>
      <polygon points="12,0 38,0 30,30 2,30" fill="var(--paper)"/>
      <path d="M14 15 H25 M21 11 L25 15 L21 19" stroke="var(--ink-deep)" stroke-width="1.8" fill="none"/>
    </svg>
    <span class="location-tag__name">WEINSTADT</span>
  </div>
</main>
</body>
</html>
```